Business Card Design Project

Require a business card for a swing band called "Brass and Lantern". We are a 6 piece band that performs at events and corporate functions. Our music is great for dancing to or just providing a classy background atmosphere for people to enjoy. Final design should communicate professionalism and style with a hint of fun.

Sorry, just realised that it needs to be single sided only. Also, no rounded edges.

Industry/Entity Type

Events

Requirements
Must have
• Contact number: 0438 216 903
email address: brassandlantern@mailpost.example
Website details: www.brassandlantern.example

```html
<!DOCTYPE html>
<html lang="en">
<head>
<meta charset="utf-8">
<title>Brass and Lantern – Business Card</title>
<link rel="stylesheet" href="https://fonts.googleapis.com/css2?family=Open+Sans:wght@400;700;800&display=swap">
<style>
  :root {
    --backdrop-dark: #120304;
    --backdrop-red: #4a0a10;
    --photo-purple: #8a2a9a;
    --photo-magenta: #b1309a;
    --photo-red: #6a0f1c;
    --photo-black: #1a0612;
    --ink-white: #ffffff;
    --bar-ink: #f2eef4;
    --icon-grey: #8d8a90;
    --icon-fill: #555059;
    --card-edge: #d9d6dc;
  }
  * { box-sizing: border-box; margin: 0; padding: 0; }
  html, body {
    width: 1200px; height: 900px; overflow: hidden;
    background: var(--backdrop-dark);
    font-family: "Open Sans", Arial, sans-serif;
  }
  .presentation {
    position: relative; width: 1200px; height: 900px; overflow: hidden;
    background: radial-gradient(ellipse at 30% 70%, var(--backdrop-red), var(--backdrop-dark) 70%);
  }

  /* Detail view below the card */
  .detail-view {
    position: absolute; left: 344px; top: 600px; width: 856px; height: 300px;
    background: linear-gradient(120deg, var(--photo-purple), var(--photo-red) 55%, var(--photo-black));
    overflow: hidden;
  }
  .detail-view__name {
    position: absolute; left: 56px; top: -10px;
    font-size: 300px; font-weight: 800; line-height: 1;
    color: var(--ink-white); white-space: nowrap;
  }
  .detail-label {
    position: absolute; left: 150px; top: 780px;
    font-size: 44px; font-weight: 400; color: var(--ink-white);
    text-shadow: 0 0 10px #000, 0 0 4px #000;
  }

  /* Business card */
  .business-card {
    position: absolute; left: 14px; top: 14px; width: 1058px; height: 606px;
    border: 2px solid var(--card-edge);
    overflow: hidden;
  }
  .business-card__photo {
    position: absolute; inset: 0;
    background:
      radial-gradient(ellipse at 80% 15%, #d7b6dc 0, transparent 30%),
      radial-gradient(ellipse at 20% 80%, var(--photo-red), transparent 55%),
      linear-gradient(135deg, var(--photo-magenta), var(--photo-purple) 45%, var(--photo-red) 80%, var(--photo-black));
  }
  .business-card__name {
    position: absolute; left: 30px; top: 250px; width: 994px;
    text-align: center;
    font-size: 96px; font-weight: 800; line-height: 1.1;
    color: var(--ink-white); white-space: nowrap;
  }
  .contact-bar {
    position: absolute; left: 0; right: 0; bottom: 0; height: 44px;
    background: rgba(20, 4, 14, 0.55);
    display: flex; align-items: center; justify-content: space-between;
    padding: 0 14px;
    font-size: 21px; color: var(--bar-ink); white-space: nowrap;
  }
  .contact-bar__item { display: flex; align-items: center; gap: 8px; }
  .contact-bar__icon {
    width: 26px; height: 26px; border: 2px solid var(--icon-grey);
    background: var(--icon-fill); color: #ddd; font-size: 16px; font-weight: 700;
    display: flex; align-items: center; justify-content: center;
  }
  .contact-bar__divider { color: var(--bar-ink); }
</style>
</head>
<body>
  <main class="presentation">
    <section class="detail-view" role="img" aria-label="Enlarged detail of the band name over the crowd photograph">
      <div class="detail-view__name">Brass</div>
    </section>
    <p class="detail-label">In 100%</p>

    <article class="business-card">
      <div class="business-card__photo" role="img" aria-label="Photograph of a dancing crowd at a live band event, tinted purple and red"></div>
      <h1 class="business-card__name">Brass and Lantern</h1>
      <footer class="contact-bar">
        <span class="contact-bar__item"><span class="contact-bar__icon">P</span>0438 216 903</span>
        <span class="contact-bar__divider">|</span>
        <span class="contact-bar__item"><span class="contact-bar__icon">E</span>brassandlantern@mailpost.example</span>
        <span class="contact-bar__divider">|</span>
        <span class="contact-bar__item"><span class="contact-bar__icon">W</span>www.brassandlantern.example</span>
      </footer>
    </article>
  </main>
</body>
</html>
```